Business Cards and Stationary for Dental Office
Modern dental office
I need double sided standard sized Business Card [3.5" x 2"]
You can use either the same font, or change it up--as long as it looks good
Bright & Fun-filled
Folasade Ikeribe DDS
Dr.
5128 Marlow Ave
Suite 340
Baltimore, MD 21207
TBD
Info@mycedarlinedental.com
www.mycedarlinedental.com
The phone number is tbd
Please note this as I will ask for it to be added at a later date. Thanks
This is my logo in AI

```html
<!DOCTYPE html>
<html lang="en">
<head>
<meta charset="utf-8">
<title>Cedarline Dental Care – Business Card</title>
<link href="https://fonts.googleapis.com/css2?family=Cinzel:wght@400;600&display=swap" rel="stylesheet">
<style>
  :root{
    --backdrop:#e9e9e7;
    --card:#ffffff;
    --ink-gray:#6d6e70;
    --bar-gray:#7a7b7d;
    --mint:#a8dcb4;
    --green:#79c48c;
    --white:#ffffff;
  }
  html,body{margin:0;padding:0;overflow:hidden}
  body{width:1200px;height:902px;background:var(--backdrop);position:relative;font-family:"Cinzel",serif}
  .card{position:absolute;left:100px;top:165px;width:1000px;height:572px;background:var(--card);box-shadow:0 6px 24px rgba(0,0,0,.12);overflow:hidden}
  .brand-mark{position:absolute;left:456px;top:58px;width:88px;height:88px;border-radius:50%;background:var(--mint)}
  .brand-name{position:absolute;left:0;right:0;top:166px;text-align:center;font-size:38px;color:var(--ink-gray);letter-spacing:1px;margin:0;font-weight:400}
  .brand-location{position:absolute;left:0;right:0;top:216px;text-align:center;font-size:13px;color:var(--green);letter-spacing:1.5px;margin:0}
  .doctor-line{position:absolute;left:0;right:0;top:264px;text-align:center;font-size:22px;color:var(--green);margin:0}
  .doctor-line .sep{color:var(--ink-gray)}
  .contact-row{position:absolute;left:95px;right:95px;display:flex;justify-content:space-between;align-items:center;font-size:15px;color:var(--ink-gray)}
  .row-one{top:320px}
  .row-two{top:356px}
  .item{display:flex;align-items:center;gap:8px;white-space:nowrap}
  .phones{gap:20px}
  .item svg{width:20px;height:20px;flex:none}
  .band-right{position:absolute;right:0;top:395px;width:150px;height:16px;background:var(--mint)}
  .band-left{position:absolute;left:0;top:440px;width:290px;height:16px;background:var(--mint)}
  .web-bar{position:absolute;left:290px;top:418px;width:560px;height:40px;background:var(--bar-gray);display:flex;align-items:center;justify-content:center;color:var(--white);font-size:13px;letter-spacing:3px}
</style>
</head>
<body>
  <div class="card">
    <div class="brand-mark" aria-hidden="true"></div>
    <h1 class="brand-name">Cedarline Dental Care</h1>
    <p class="brand-location">at Harborview Hospital Baltimore MD</p>
    <p class="doctor-line">Folasade Ikeribe DDS <span class="sep">|</span> Dr.Folasade</p>

    <div class="contact-row row-one">
      <span class="item">
        <svg viewBox="0 0 20 20"><circle cx="10" cy="10" r="10" fill="#79c48c"/><path d="M10 4.5a3.5 3.5 0 0 0-3.5 3.5c0 2.6 3.5 7 3.5 7s3.5-4.4 3.5-7A3.5 3.5 0 0 0 10 4.5zm0 4.8a1.3 1.3 0 1 1 0-2.6 1.3 1.3 0 0 1 0 2.6z" fill="#fff"/></svg>
        5128 Marlow Ave. Suite 340 Baltimore, MD 21207
      </span>
      <span class="item">
        <svg viewBox="0 0 20 20"><circle cx="10" cy="10" r="10" fill="#79c48c"/><circle cx="10" cy="10" r="5" fill="none" stroke="#fff" stroke-width="1.3"/><path d="M5 10h10M10 5c-2 3-2 7 0 10M10 5c2 3 2 7 0 10" fill="none" stroke="#fff" stroke-width="1"/></svg>
        www.mycedarlinedental.com
      </span>
    </div>

    <div class="contact-row row-two">
      <span class="item phones">
        <span class="item">
          <svg viewBox="0 0 20 20"><circle cx="10" cy="10" r="10" fill="#79c48c"/><path d="M7 5l2 2.5-1 1.3c.7 1.4 1.8 2.5 3.2 3.2l1.3-1 2.5 2-1 1.5c-3.8-.4-7.1-3.7-7.5-7.5z" fill="#fff"/></svg>
          555-201-4480
        </span>
        <span class="item">
          <svg viewBox="0 0 20 20"><circle cx="10" cy="10" r="10" fill="#79c48c"/><rect x="6" y="5" width="8" height="10" rx="1" fill="#fff"/><rect x="7.5" y="6.5" width="5" height="3" fill="#79c48c"/></svg>
          555-318-9027
        </span>
      </span>
      <span class="item">
        <svg viewBox="0 0 20 20"><circle cx="10" cy="10" r="10" fill="#79c48c"/><rect x="5" y="6.5" width="10" height="7" fill="#fff"/><path d="M5 6.5l5 4 5-4" fill="none" stroke="#79c48c" stroke-width="1"/></svg>
        Info@mycedarlinedental.com
      </span>
    </div>

    <div class="band-right"></div>
    <div class="web-bar">www.mycedarlinedental.com</div>
    <div class="band-left"></div>
  </div>
</body>
</html>
```